Grindstones- Tattoos/Piercings/Motorcycle/Biker Appearl Shop

Grindstones' buisness cards can be creative, playful and eye catching. Incorporate leather or diamond plate. We are an all female business. Biker theme, Tattoo Photos, Piercing Photos, Diamond plate, Leather and Girls!

This project needs to be an appointment card as well for the tattoo artists and piercers. We need a section that says APPT With: _______ , DATE, TIME, and then a QUOTE and DEPOSIT section for the artists. I attached the logo so you could incorportate that and have complete creative freedom. It's a biker store, we sell biker appearl and accessories, with a tattoo and piercing shop connected. Girls, Leather, Tattoos and Piercings. Have fun with it!
Updates

I've Updated project details for better description of what im looking for. Thanks!

Target Market(s)

Male and Female Ages 15-90. Interests in custom tattoos and quality piercings, bikers, motorcycle accessories like helmets, gloves, masks, leather, boots. Jewlery and clothes.

Industry/Entity Type

Business

Contact Information for Business Card

The business is called Grindstones, address, phone number and website. (2847 Larkmoor Rd. Muskegon, MI. 49517 (231)870-4152 www.inkvalleyshop.example)

Font styles to use
Serif
Sans Serif
Decorative
Script

Requirements
Must have
• Appointment with______
• Date_____ or MON TUES WED THUR etc... check mark boxes
• Time_____
• Quote______
• Deposit_______
• (231) 870-4152
• 2847 Larkmoor Rd
• Muskegon, MI 49517
• a facebook logo
Nice to have
• Owner Roy Pemberly
Should not have
• Tribal dragons or anything Tribal.That's cheesy! No Butterflies, No stars. No boys,

```html
<!DOCTYPE html>
<html lang="en">
<head>
<meta charset="utf-8">
<title>Grindstones – Business &amp; Appointment Card</title>
<link rel="stylesheet" href="https://fonts.googleapis.com/css2?family=Cinzel:wght@700;900&family=Open+Sans:wght@700;800&display=swap">
<style>
  :root {
    --stage: #d9d9d9;
    --maroon-deep: #3a0d0c;
    --maroon: #6e2418;
    --tan: #b08a5a;
    --cream: #efe6c4;
    --cream-pale: #f6efd6;
    --umber: #6b4322;
    --edge-dark: #1b0f0b;
    --ink: #1a1512;
    --tag-red: #a3141a;
    --phone-red: #e0191e;
    --web-green: #5bc236;
    --logo-gold: #f3e2b8;
    --plate: #c69a62;
    --plate-dark: #8c6236;
    --icon-blue: #3b5a98;
    --pillar-dark: #0f0a08;
    --pillar-mid: #4a3f38;
  }
  * { box-sizing: border-box; margin: 0; padding: 0; }
  html, body {
    width: 1200px; height: 747px; overflow: hidden;
    background: var(--stage);
  }
  .stage {
    position: relative; width: 1200px; height: 747px;
    display: flex; justify-content: center; align-items: center; gap: 44px;
  }
  .card {
    position: relative; width: 378px; height: 660px; overflow: hidden;
    background:
      radial-gradient(ellipse 75% 70% at 50% 55%, rgba(27,15,11,0) 62%, rgba(27,15,11,0.75) 100%),
      radial-gradient(ellipse 90% 50% at 50% 64%, var(--cream-pale) 0%, rgba(239,230,196,0.9) 40%, rgba(239,230,196,0) 78%),
      linear-gradient(180deg, var(--maroon-deep) 0%, var(--maroon) 24%, var(--tan) 48%, #c9ab78 68%, var(--umber) 92%, var(--edge-dark) 100%);
    box-shadow: 0 6px 18px rgba(0,0,0,0.35);
    font-family: "Open Sans", Arial, sans-serif;
    text-align: center;
  }
  .brand {
    position: relative; margin-top: 26px;
    font-family: "Cinzel", Georgia, serif; font-weight: 900;
    font-size: 40px; color: var(--logo-gold); letter-spacing: 1px;
  }
  .emblem {
    position: relative; display: block; margin: 22px auto 0;
    border-radius: 8px;
  }
  .emblem--skull {
    width: 150px; height: 120px;
    background: radial-gradient(circle, #f0a23a, #8a4a1c 60%, rgba(110,36,24,0) 72%);
  }
  .emblem--machines {
    width: 140px; height: 96px; margin-top: 18px;
    background: radial-gradient(ellipse, #e4e4e4, #8d8d8d 50%, rgba(110,36,24,0) 72%);
  }
  .tagline {
    position: relative; margin-top: 36px;
    font-family: "Cinzel", Georgia, serif; font-weight: 700;
    font-size: 12px; line-height: 27px; text-transform: uppercase; white-space: nowrap;
  }
  .tagline .red { color: var(--tag-red); }
  .tagline .dark { color: var(--ink); }
  .nameplate {
    position: relative; margin: 26px auto 0; width: 168px; height: 70px;
    background: linear-gradient(var(--plate), var(--plate-dark));
    border-radius: 6px; padding-top: 12px;
  }
  .nameplate__name { font-size: 19px; font-weight: 800; color: var(--ink); }
  .nameplate__role { font-size: 13px; font-weight: 700; color: var(--ink); }
  .contact { position: absolute; left: 0; right: 0; bottom: 24px; }
  .contact__phone { font-size: 28px; font-weight: 700; color: var(--phone-red); }
  .contact__address { margin-top: 6px; font-size: 13px; font-weight: 800; color: var(--ink); }
  .contact__web { margin-top: 10px; font-size: 17px; font-weight: 800; color: var(--web-green); }

  .pillar {
    position: absolute; top: 0; width: 44px; height: 400px;
    background: linear-gradient(90deg, var(--pillar-dark), var(--pillar-mid) 50%, var(--pillar-dark));
    -webkit-mask-image: linear-gradient(180deg, #000 70%, transparent 100%);
    mask-image: linear-gradient(180deg, #000 70%, transparent 100%);
  }
  .pillar--left { left: 0; }
  .pillar--right { right: 0; }
  .appt {
    position: relative; margin: 26px 54px 0; text-align: left;
    font-family: "Cinzel", Georgia, serif; font-weight: 700; color: var(--ink);
  }
  .appt__title { text-align: center; font-size: 20px; }
  .appt__line { display: block; height: 2px; background: var(--ink); }
  .appt__title-line { width: 190px; margin: 22px 0 0 auto; }
  .appt__row { display: flex; align-items: flex-end; margin-top: 14px; font-size: 20px; }
  .appt__row .appt__line { flex: 1; margin-left: 14px; margin-bottom: 6px; }
  .social-square {
    position: relative; display: block; margin: 40px auto 0;
    width: 16px; height: 16px; background: var(--icon-blue);
  }
</style>
</head>
<body>
<main class="stage">
  <section class="card card--business">
    <div class="brand">Grindstones</div>
    <div class="emblem emblem--skull" role="img" aria-label="Flaming skull with motorcycle handlebars emblem"></div>
    <p class="tagline">
      <span class="red">Biker appearl and accessories,</span><br>
      <span class="red">with a tattoo and piercing shop connected.</span><br>
      <span class="dark">Girls, leather, tattoos and piercings</span>
    </p>
    <div class="nameplate">
      <div class="nameplate__name">Roy Pemberly</div>
      <div class="nameplate__role">Owner</div>
    </div>
    <div class="contact">
      <div class="contact__phone">(231)870-4152</div>
      <div class="contact__address">2847 LARKMOOR RD. MUSKEGON, MI. 49517</div>
      <div class="contact__web">WWW.INKVALLEYSHOP.EXAMPLE</div>
    </div>
  </section>

  <section class="card card--appointment">
    <div class="pillar pillar--left" role="img" aria-label="Stone pillar wrapped by a serpent"></div>
    <div class="pillar pillar--right" role="img" aria-label="Stone pillar wrapped by a serpent"></div>
    <div class="brand">Grindstones</div>
    <div class="emblem emblem--machines" role="img" aria-label="Crossed tattoo machines with wings"></div>
    <div class="appt">
      <div class="appt__title">Appointment With</div>
      <span class="appt__line appt__title-line"></span>
      <div class="appt__row">Date<span class="appt__line"></span></div>
      <div class="appt__row">Time<span class="appt__line"></span></div>
      <div class="appt__row">Quote<span class="appt__line"></span></div>
      <div class="appt__row">Deposit<span class="appt__line"></span></div>
    </div>
    <span class="social-square"></span>
    <div class="contact">
      <div class="contact__phone">(231)870-4152</div>
      <div class="contact__address">2847 LARKMOOR RD. MUSKEGON, MI. 49517</div>
      <div class="contact__web">WWW.INKVALLEYSHOP.EXAMPLE</div>
    </div>
  </section>
</main>
</body>
</html>
```